依頼詳細
新メニュー「翠雨のひととき」を周知するためのチラシです。高級感とラグジュアリー感を大事にしたいです。チラシご持参の方に1000円の割引をつける予定です。
記載項目
社名、メールアドレス、URL、添付ファイル内容
サイズ
A5
ページ数
両面
希望イメージ
• +5 0 +5
• シンプル
複雑
• 単色
カラフル
• 暗い
明るい
• 日常
高級
• 遊び心
厳粛
• 未来的
伝統的
• 女性的
男性的
希望する色
茶系、グレー系、紫系
納品ファイル
• 高解像度JPG (.jpg)
• イラストレーター形式 (.ai)
補足説明
依頼公開後の追記内容
自作のパワーポイントで作ったものを添付済みです。
プロのセンスでA5版両面にまとめてください。
●期日を2日延長します
18日まで!

●添付したA4パワポの画像について
別に添付した写真に変更したいです
(すでにご提案いただいた方は、ひとまず現状のままで大丈夫です。ありがとうございます。)

ステキなご提案お待ちしています(^^)
■ 選んだ理由

高級感のある洗練されたデザインです。
よりわかりやすく、より伝わりやすくアレンジを加えてくださいました。
寄り添ってくださる感じが、特に決め手となりました。

■ 提案者全員のお礼・コメント

ご提案くださった皆様、ありがとうございます。
どのご提案も、オリジナリティにあふれた素晴らしいデザインでした。
機会がありましたら、どうぞまたよろしくお願いいたします。

```html
<!DOCTYPE html>
<html lang="ja">
<head>
<meta charset="utf-8">
<title>翠雨のひととき</title>
<link rel="stylesheet" href="https://fonts.googleapis.com/css2?family=Cormorant+Garamond:wght@500;600&family=Noto+Serif+JP:wght@400;500;700&family=Noto+Sans+JP:wght@400;500&display=swap">
<style>
  :root{
    --ink-deep:#1a0f24;
    --plum:#2d1840;
    --violet:#4a2a6e;
    --lilac:#8a62c0;
    --gold:#d9b774;
    --gold-soft:#c9a863;
    --gold-glow:#f1dca6;
    --text-light:#f3ecf7;
    --text-dark:#3a2614;
    --paper:#ffffff;
    --grey-text:#6b6470;
  }
  *{margin:0;padding:0;box-sizing:border-box}
  html,body{width:875px;height:1200px;overflow:hidden;background:var(--ink-deep)}
  .flyer{
    position:relative;width:875px;height:1200px;overflow:hidden;
    background:
      radial-gradient(ellipse 520px 240px at 160px 1040px, rgba(138,98,192,.55), transparent 70%),
      radial-gradient(ellipse 480px 220px at 730px 1060px, rgba(138,98,192,.45), transparent 70%),
      linear-gradient(180deg,#140b1c 0%, var(--plum) 45%, var(--violet) 88%);
    font-family:"Noto Serif JP",serif;color:var(--text-light);
  }
  .hero-photo{
    position:absolute;left:0;top:0;width:875px;height:470px;
    background:
      radial-gradient(ellipse 300px 160px at 600px 150px, rgba(240,190,140,.35), transparent 70%),
      radial-gradient(ellipse 260px 120px at 180px 240px, rgba(120,100,150,.35), transparent 70%),
      linear-gradient(180deg,#2a2024 0%,#3a2c2a 40%,#24182a 80%,rgba(45,24,64,0) 100%);
  }
  .tagline{
    position:absolute;top:28px;left:0;width:100%;
    display:flex;align-items:center;justify-content:center;gap:18px;
    font-family:"Cormorant Garamond",serif;font-weight:600;
    font-size:19px;letter-spacing:.28em;color:var(--text-light);
  }
  .tagline::before,.tagline::after{content:"";width:150px;height:1px;background:rgba(243,236,247,.7)}
  .title-block{position:absolute;top:385px;left:0;width:100%;text-align:center}
  .title{
    font-size:76px;font-weight:500;color:var(--gold);letter-spacing:.04em;line-height:1.2;
    text-shadow:0 0 18px rgba(0,0,0,.6);
  }
  .subtitle{margin-top:10px;font-size:24px;color:var(--gold);letter-spacing:.06em}
  .lead{margin-top:12px;font-size:16px;letter-spacing:.04em}
  .features{position:absolute;top:620px;left:0;width:100%;height:330px}
  .feature{
    position:absolute;top:0;width:320px;height:320px;border-radius:50%;
    border:2px solid var(--gold);
    background:radial-gradient(circle, var(--gold-glow) 0%, rgba(217,183,116,.85) 45%, rgba(60,34,70,.9) 100%);
    text-align:center;padding:62px 58px 0;color:var(--text-dark);
  }
  .feature--left{left:110px}
  .feature--right{left:445px}
  .feature-name{font-size:18px;font-weight:700;padding-bottom:10px;border-bottom:1px solid var(--text-dark);margin:0 12px 16px}
  .feature-text{font-size:15px;line-height:1.8;font-weight:500}
  .times{position:absolute;left:407px;top:130px;width:60px;height:60px}
  .details{position:absolute;top:985px;left:100px;width:675px;display:flex;gap:45px}
  .details p{flex:1;font-size:13.5px;line-height:1.8;text-align:justify}
  .footer{
    position:absolute;left:0;bottom:0;width:100%;height:95px;background:var(--paper);
    display:flex;align-items:center;justify-content:space-between;padding:0 60px;
  }
  .brand{color:var(--violet)}
  .brand-name{font-family:"Noto Serif JP",serif;font-size:32px;font-weight:500;line-height:1.1}
  .brand-sub{font-size:11px;color:var(--grey-text);margin-top:4px}
  .more{display:flex;align-items:center;gap:10px;font-family:"Noto Sans JP",sans-serif;font-size:14px;color:var(--grey-text)}
</style>
</head>
<body>
<main class="flyer">
  <div class="hero-photo" role="img" aria-label="暗い照明の施術室でリクライニングベッドに横たわる利用者の写真"></div>
  <p class="tagline">HIGH-QUALITY SLEEP × SPECIAL CARE</p>

  <header class="title-block">
    <h1 class="title">翠雨のひととき</h1>
    <p class="subtitle">ゼログラビティ × ホルミシス体感</p>
    <p class="lead">「上質な眠り」と「格別のケア」をお届けするボディメンテナンスです。</p>
  </header>

  <section class="features">
    <div class="feature feature--left">
      <h2 class="feature-name">ゼログラビティ</h2>
      <p class="feature-text">宇宙工学の理論に着想した理想の体勢。体圧分散に優れた姿勢での深い眠りによってストレスを解消します。</p>
    </div>
    <div class="feature feature--right">
      <h2 class="feature-name">ホルミシス体感</h2>
      <p class="feature-text">ラジウムから放出される微量の放射線は細胞を活性化させます。心身の様々な良い作用を体感してください。</p>
    </div>
    <svg class="times" viewBox="0 0 60 60" aria-hidden="true">
      <path d="M6 6 L54 54 M54 6 L6 54" stroke="#f3ecf7" stroke-width="2"/>
    </svg>
  </section>

  <section class="details">
    <p>130°の体勢角度は、無重力時の自然な姿勢となり、宇宙空間にいるような浮遊感を得られます。首、背中、腰に負荷のない最小の姿勢と筋肉で、究極の深睡眠によってストレスが解消されます。</p>
    <p>「奇跡の温泉」と称される北嶺の湯や白砂の湯。ラドン浴でも注目される欧州の坑道と同様、ホルミシス作用が得られる空間をぜひお試しください。</p>
  </section>

  <footer class="footer">
    <div class="brand">
      <div class="brand-name">Velluna</div>
      <div class="brand-sub">ボディケア専門</div>
    </div>
    <div class="more">
      <span>詳しい内容は裏面をご覧ください。</span>
      <svg width="22" height="22" viewBox="0 0 22 22" aria-hidden="true">
        <circle cx="11" cy="11" r="10" fill="#4a2a6e"/>
        <path d="M9 6 L14 11 L9 16" stroke="#fff" stroke-width="2" fill="none"/>
      </svg>
    </div>
  </footer>
</main>
</body>
</html>
```